Health and Wellness company needs flyer to promote free seminar

Corelift studio is a health and wellness company that offers an exercise program designed by physical therapists to help relieve pain and improve mobility. Our business is a new concept that is not well understood by the public. In order to promote our business we offer a free seminar where we present information regarding the underlying cause of pain and tightness. During the seminar we also perform a posture screen and movement testing for all participants.

Target Market(s)

Mostly healthy and active women ages 25-65

Industry/Entity Type

Health And Wellness

Font styles to use
Sans Serif

Colors

Designer to choose colors to be used in the design.

Requirements
Must have
• Title: Eliminate Pain and Tightness For Good
• Paragraph: Corelift Studio offers a free 60 minute seminar: "The Busy Walker's Handbook to Stretching and Standing Taller."
• What to Expect:
• • Identify the underlying cause of your pain and mobility issues
• • Expose what gets in the way of you moving and feeling better
• • Learn why traditional exercises don’t help and can actually make the problem worse
• • Reveal what your posture is saying and how that impacts you
• • Experience your muscle imbalances through movement tests
• • Discover the training method that realigns your posture, increases your mobility and reduces your pain
• Call to action: RSVP online at coreliftstudio.com
Nice to have
• Use a relevant image showing a female dealing with tightness in the low back, legs, etc.
• Emphasize that the seminar is FREE.
• Make the call to action prominent.

```html
<!DOCTYPE html>
<html lang="en">
<head>
<meta charset="utf-8">
<title>Corelift Studio – Free 60 Minute Seminar</title>
<link rel="stylesheet" href="https://fonts.googleapis.com/css2?family=Montserrat:wght@700;800;900&family=Open+Sans:wght@600&family=Libre+Baskerville:wght@700&display=swap">
<style>
  :root{
    --navy:#3b3b6b;
    --orange:#f7941d;
    --red:#e31e24;
    --grey:#a6a6a6;
    --ink:#2e2e4a;
    --white:#ffffff;
  }
  html,body{margin:0;padding:0;overflow:hidden;background:#fff;}
  .flyer{position:relative;width:846px;height:1200px;overflow:hidden;background:var(--white);font-family:"Open Sans",sans-serif;}
  .print-mark{position:absolute;top:14px;right:26px;font:800 24px "Montserrat",sans-serif;color:#c8c8c8;letter-spacing:1px;}
  .brand{position:absolute;top:52px;left:0;width:846px;display:flex;justify-content:center;align-items:center;gap:16px;}
  .brand-square{width:58px;height:58px;background:var(--orange);}
  .brand-name{font:800 50px "Montserrat",sans-serif;color:var(--navy);letter-spacing:-1px;}
  .headline{position:absolute;top:141px;left:25px;width:781px;height:46px;margin:0;background:var(--navy);color:var(--white);
    display:flex;align-items:center;justify-content:center;font:800 32px "Montserrat",sans-serif;letter-spacing:.3px;white-space:nowrap;}
  .headline em{font-style:normal;color:var(--orange);}
  .backdrop{position:absolute;inset:0;}
  .photo{position:absolute;left:446px;top:265px;width:400px;height:722px;border-radius:170px 0 0 0;
    background:linear-gradient(180deg,#7a5440 0%,#9b6c52 14%,#e3b9a8 24%,#d9b0ae 55%,#cfa3a4 85%,#c9c4c8 100%);}
  .burst{position:absolute;left:156px;top:344px;width:0;height:0;}
  .burst span{position:absolute;left:-98px;top:-98px;width:196px;height:196px;background:var(--orange);}
  .burst span:nth-child(2){transform:rotate(15deg);}
  .burst span:nth-child(3){transform:rotate(30deg);}
  .burst span:nth-child(4){transform:rotate(45deg);}
  .burst span:nth-child(5){transform:rotate(60deg);}
  .burst span:nth-child(6){transform:rotate(75deg);}
  .burst-text{position:absolute;left:56px;top:258px;width:210px;margin:0;transform:rotate(-9deg);font-family:"Montserrat",sans-serif;line-height:1;}
  .burst-free{display:block;font-weight:900;font-size:62px;color:var(--red);letter-spacing:2px;}
  .burst-minutes{display:block;font-weight:800;font-size:31px;color:var(--white);margin-top:4px;}
  .burst-seminar{display:block;font-weight:900;font-size:37px;color:var(--navy);margin-top:2px;}
  .expect{position:absolute;left:26px;top:512px;width:410px;color:var(--white);}
  .expect h2{margin:0 0 20px;font:700 22px Arial,Helvetica,sans-serif;}
  .expect ul{list-style:none;margin:0;padding:0;}
  .expect li{position:relative;padding-left:21px;margin-bottom:22px;font-size:19px;line-height:22px;font-weight:600;white-space:nowrap;}
  .expect li svg{position:absolute;left:3px;top:8px;}
  .expect li u{text-underline-offset:3px;}
  .seminar-title{position:absolute;left:10px;top:1040px;width:540px;text-align:center;margin:0;
    font:700 27px/40px "Libre Baskerville",serif;color:var(--ink);white-space:nowrap;}
  .cta-label{position:absolute;left:576px;top:1020px;width:270px;height:52px;background:var(--orange);border-radius:28px 0 0 0;
    display:flex;align-items:center;justify-content:center;font:900 21px "Montserrat",sans-serif;color:#111;}
  .cta-url{position:absolute;left:544px;top:1066px;width:302px;height:54px;background:var(--navy);border-radius:0 0 0 28px;
    display:flex;align-items:center;justify-content:center;font:800 20px "Montserrat",sans-serif;color:var(--white);}
</style>
</head>
<body>
<main class="flyer">
  <div class="print-mark">RGB</div>

  <header class="brand">
    <span class="brand-square"></span>
    <span class="brand-name">Corelift studio</span>
  </header>

  <h1 class="headline">ELIMINATE&nbsp;<em>PAIN</em>&nbsp;&amp;&nbsp;<em>TIGHTNESS</em>&nbsp;FOR GOOD</h1>

  <svg class="backdrop" width="846" height="1200" viewBox="0 0 846 1200" aria-hidden="true">
    <path fill="var(--navy)" d="M0 452 L40 446 L44 450 L90 440 L130 436 L134 441 L180 428 L230 420 L236 425 L290 410 L340 400 L346 404 L400 390 L450 382 L456 386 L510 372 L560 364 L566 368 L620 356 L680 348 L686 352 L740 342 L800 336 L806 340 L846 332
      L846 958 L800 962 L796 966 L740 970 L690 976 L684 972 L620 982 L560 990 L554 986 L490 996 L430 1002 L424 998 L360 1008 L300 1014 L294 1010 L230 1018 L170 1024 L164 1020 L100 1028 L40 1032 L34 1028 L0 1032 Z"/>
  </svg>

  <div class="photo" role="img" aria-label="Photo of a woman from behind in a pink tank top, hands pressed to her aching lower back"></div>

  <div class="burst" aria-hidden="true"><span></span><span></span><span></span><span></span><span></span><span></span></div>
  <p class="burst-text">
    <span class="burst-free">FREE</span>
    <span class="burst-minutes">60 minute</span>
    <span class="burst-seminar">SEMINAR</span>
  </p>

  <section class="expect">
    <h2>WHAT TO EXPECT</h2>
    <ul>
      <li><svg width="9" height="7" viewBox="0 0 9 7"><path d="M1 3.5 L3.5 6 L8 1" fill="none" stroke="var(--orange)" stroke-width="2"/></svg><u>IDENTIFY</u> the underlying cause of<br>your pain and mobility issues.</li>
      <li><svg width="9" height="7" viewBox="0 0 9 7"><path d="M1 3.5 L3.5 6 L8 1" fill="none" stroke="var(--orange)" stroke-width="2"/></svg><u>EXPOSE</u> what gets in the way of<br>you moving and feeling better.</li>
      <li><svg width="9" height="7" viewBox="0 0 9 7"><path d="M1 3.5 L3.5 6 L8 1" fill="none" stroke="var(--orange)" stroke-width="2"/></svg><u>LEARN</u> why traditional exercises don’t<br>help and can actually make the<br>problem worse.</li>
      <li><svg width="9" height="7" viewBox="0 0 9 7"><path d="M1 3.5 L3.5 6 L8 1" fill="none" stroke="var(--orange)" stroke-width="2"/></svg><u>REVEAL</u> what your posture is saying<br>and how that impacts you.</li>
      <li><svg width="9" height="7" viewBox="0 0 9 7"><path d="M1 3.5 L3.5 6 L8 1" fill="none" stroke="var(--orange)" stroke-width="2"/></svg><u>EXPERIENCE</u> your muscle imbalances<br>through movement tests.</li>
      <li><svg width="9" height="7" viewBox="0 0 9 7"><path d="M1 3.5 L3.5 6 L8 1" fill="none" stroke="var(--orange)" stroke-width="2"/></svg><u>DISCOVER</u> the training method that<br>realigns your posture, increases your<br>mobility and reduces your pain.</li>
    </ul>
  </section>

  <p class="seminar-title">“The Busy Walker's Handbook to<br>Stretching and Standing Taller”</p>

  <div class="cta-label">RSVP online at</div>
  <div class="cta-url">coreliftstudio.com</div>
</main>
</body>
</html>
```